website for local kavenda practicioner and yoga teacher trainer

The website should function primarily as:
A place where people can discover Kavenda and book sessions.
A central hub connecting all of my work.
A professional home that reflects my personality and approach.
Website design for Liesbet Oonwerk — Kavenda® Structural Integration practitioner, movement educator, yoga teacher and teacher trainer.
A website that can grow with future projects.
The website should feel: Warm, Human, Invitational, Professional, Accessible, Intelligent, Calm, Clear, Playful, Exploratory, Trustworthy
Avoid: New age aesthetics, Mystical clichés, Excessive spirituality, ”Guru" vibes, Overly clinical design, Corporate wellness branding, Busy layouts
Think: modern, grounded, curious and real.
My work combines three interconnected areas:
1.Bodywork: Touch, structure, awareness and one-on-one support.
2. Movement: Yoga, Pilates and embodied movement.
3. Education: Teacher trainings, workshops and continued learning.
Underlying values:
Curiosity over certainty
Possibility over perfection
Complexity without overwhelm
Science and lived experience together
Exploration rather than dogma
Human beings before methods
The primary goal of the website is to introduce people to Kavenda® Structural Integration and make it easy for them to:
Understand what Kavenda is
Discover whether it might be relevant for them
Learn what to expect from a session
Book an appointment
Booking should always feel visible and easy.
Secondary Goal: Present all other aspects of my work in one coherent place:
Yoga classes
Pilates classes
Teacher trainings
Workshops
Retreats
One-on-one movement sessions
Collaborations with studios
Website Structure
1: HOME
1.1.Hero Section: Large welcoming image
1.2 Two Main Pathways
- Bodywork: Kavenda® Structural Integration
- Movement & Education: Yoga, Pilates, trainings, workshops and retreats
- About Preview: Small introduction with portrait. + Button:
Read More
1.3 Current Events / What's Coming Up: Upcoming trainings, workshops and retreats. (This section should be easy to update)
1.4. Contact / Newsletter: Simple contact information
2: Kavenda® Structural Integration
What is Kavenda?
For whom is it?
What does a session look like?
FAQ
Prices
Booking
Future possibility:
Kaven Movement sessions
3: Movement
- Introductory text.
- Studio Classes (link to “my home base” - > local yoga studio)
- One-to-One Sessions: booking option (this is small; not a key aspect I want to promote)
- Workshops/ Retreats / Teacher Trainings => This section should be flexible and easy to update. Visitors should be able to click into specific offerings.
4. Events
Dynamic page for: Teacher trainings, Retreats, Workshops (see section in movement; here more elaborate)
Each event should contain: Image, Short description, Location, Date, Button for more information. (Linking to hosting studio/location)
5. Work With Me
For studios, organisations and teacher training schools.
Examples: Guest teaching, Workshops, Anatomy, Sequencing, Teacher development , Continuing education -> Clear call-to-action.
Call to action!!=> Book a Session
Prominent button in the navigation.
Footer:
- About Me: Longer biography (6th page)
Personal story and background.
- Testimonials (7th page): Separate page containing testimonials from:
Kavenda clients
Students
Teacher trainees
- Contact: 8th page
Visual Direction
Natural textures. Lots of white space.Editorial feeling.Professional photography.Simple navigation.
Less "wellness influencer.” More:Thoughtful, Contemporary, Timeless, Grounded, Human
Photography should show:
Teaching
Hands-on work
Natural movement
Real interaction
Simplicity
Avoid stereotypical yoga imagery and overly spiritual aesthetics.
Keywords
Warm. Curious. Human. Professional. Embodied. Intelligent. Accessible. Playful. Grounded. Exploratory. Real.
Inspiration / Core Message
Helping people feel more at home in their bodies through touch, movement and education.
The website should communicate that these are not separate services, but different expressions of the same intention:
Bodywork • Movement • Education.
Colours:
light orange/beige: e3d5c4
light orange/off white: f9f7f3
gray azure: 556b78
orange: d07b5a
grey orange: c09f80
dark grey: 3e3e3e
dark gray cyan 2f4f4f
gray green colour: a7c4a0
Fonts: Montserrat and Poppins + raleway
In added documents a try out idea of a website + logo. I will mainly use the logo with diffrent colours (image next to text).
My audience consists of people who want to feel more at home in their bodies and who appreciate a thoughtful, grounded and human approach to movement, touch and education. (30-65yo)
wellbeing
5+ page
- montserrat, poppins, raleway

```html
<!DOCTYPE html>
<html lang="en">
<head>
<meta charset="utf-8">
<title>Work with Me — Liesbet Oonwerk</title>
<link href="https://fonts.googleapis.com/css2?family=Montserrat:wght@400;500;600;700&family=Poppins:wght@400;500&display=swap" rel="stylesheet">
<style>
:root{
  --beige:#e3d5c4;
  --offwhite:#f9f7f3;
  --azure:#556b78;
  --orange:#d07b5a;
  --greyorange:#c09f80;
  --dark:#3e3e3e;
  --cyan:#2f4f4f;
  --green:#a7c4a0;
  --card-border:#ecd6cb;
}
*{margin:0;padding:0;box-sizing:border-box}
html,body{width:1200px;height:2847px;overflow:hidden;background:#fff}
body{position:relative;font-family:'Montserrat',sans-serif;color:var(--dark)}
.abs{position:absolute}

/* navigation */
.site-header{position:absolute;top:0;left:0;width:1200px;height:80px;z-index:5}
.brand{position:absolute;left:85px;top:27px;display:flex;align-items:center;gap:10px;font-size:24px;font-weight:500;color:var(--dark);white-space:nowrap}
.brand-dot{width:26px;height:26px;border-radius:50%;background:var(--greyorange);flex:none}
.nav{position:absolute;left:364px;top:37px;display:flex;gap:27px;font-size:12px;font-weight:500;white-space:nowrap}
.nav a{color:var(--dark);text-decoration:none}
.nav a.active{color:var(--orange);position:relative}
.nav a.active::before{content:"";position:absolute;left:-6px;right:-6px;top:-37px;height:3px;background:var(--orange)}
.btn-book{position:absolute;left:1005px;top:26px;width:132px;height:37px;border-radius:19px;background:var(--azure);color:#fff;font-size:12.5px;font-weight:500;display:flex;align-items:center;justify-content:center}

/* hero */
.hero-photo{position:absolute;left:0;top:0;width:1200px;height:540px;
  background:
    linear-gradient(180deg,rgba(249,245,239,.95) 0,rgba(249,245,239,.85) 70px,rgba(249,245,239,0) 150px),
    linear-gradient(100deg,#f7f1ea 0%,#f4e7d6 35%,#e9c9a3 55%,#c47a58 70%,#e8d6b8 85%,#f1e3c9 100%)}
.hero-wave{position:absolute;left:0;top:0}
.hero-text{position:absolute;left:116px;top:178px}
.eyebrow{font-size:15.5px;font-weight:500;letter-spacing:1.5px;color:var(--orange)}
.hero-title{font-size:50px;font-weight:600;margin-top:6px;color:var(--dark)}
.hero-title span{color:var(--orange)}
.hero-sub{font-family:'Poppins',sans-serif;font-size:19.5px;line-height:26px;margin-top:8px;width:400px}

/* offerings */
.ghost{position:absolute;left:0;width:1200px;top:564px;text-align:center;font-size:58px;font-weight:600;color:#f4ece3}
.section-title{position:absolute;left:0;width:1200px;top:624px;text-align:center;font-size:40px;font-weight:500}
.divider{position:absolute;height:2px;background:var(--orange)}
.divider::before,.divider::after{content:"";position:absolute;top:-2px;width:6px;height:6px;border-radius:50%;background:var(--orange)}
.divider::before{left:-3px}.divider::after{right:-3px}
.intro{position:absolute;left:160px;width:850px;top:716px;text-align:center;font-size:17.5px;line-height:22px}

.card{position:absolute;width:314px;height:290px;background:var(--offwhite);border:2px solid var(--card-border);border-radius:6px;text-align:center}
.card-icon{position:absolute;left:50%;top:-45px;margin-left:-49px;width:98px;height:98px;border-radius:50%;border:1.5px solid var(--orange);background:#fbf1ea}
.card h3{margin-top:78px;font-size:23px;font-weight:500}
.card p{margin:18px auto 0;width:296px;font-size:12.6px;line-height:19px}
.btn-start{position:absolute;left:50%;margin-left:-92px;bottom:26px;width:184px;height:44px;border-radius:22px;background:var(--orange);color:#fff;font-size:14px;font-weight:600;display:flex;align-items:center;justify-content:center;gap:6px}

/* collaborate */
.collab-text{position:absolute;left:130px;top:1804px;width:440px}
.collab-text h2{font-size:31px;font-weight:500;line-height:35px}
.collab-lead{font-size:15.5px;font-weight:600;line-height:22px;margin-top:44px;width:380px}
.collab-body{font-size:15.5px;line-height:22px;margin-top:22px;width:380px}
.btn-dark{position:absolute;left:124px;top:2107px;width:201px;height:47px;border-radius:24px;background:var(--cyan);color:#fff;font-size:14.5px;font-weight:600;display:flex;align-items:center;justify-content:center;gap:6px}

/* newsletter */
.band{position:absolute;left:0;top:2265px;width:1200px;height:229px;background:var(--cyan);color:#fff}
.band h2{position:absolute;left:112px;top:62px;font-size:30px;font-weight:600}
.band .band-sub{position:absolute;left:115px;top:110px;font-size:14.5px;line-height:19px;width:290px}
.input{position:absolute;left:415px;top:60px;width:314px;height:47px;background:#fff;color:var(--dark);font-size:13px;padding:0 18px;display:flex;align-items:center}
.btn-sub{position:absolute;left:415px;top:118px;width:314px;height:47px;background:var(--orange);font-size:14.5px;font-weight:600;display:flex;align-items:center;justify-content:center;gap:6px}
.vline{position:absolute;left:790px;top:58px;width:1px;height:112px;background:rgba(255,255,255,.3)}
.band-contact{position:absolute;left:844px;font-size:15.5px;display:flex;align-items:center;gap:10px}
.ic{width:22px;height:22px;border-radius:50%;background:#fff;display:flex;align-items:center;justify-content:center;flex:none}
.socials{display:flex;gap:5px}
.soc{width:24px;height:24px;border-radius:50%;background:#fff}

/* footer */
.foot-brand{position:absolute;left:95px;top:2540px;width:235px;text-align:center;font-size:24px;font-weight:500;color:var(--dark);white-space:nowrap}
.foot-brand .brand-dot{margin:0 auto 12px;width:50px;height:50px}
.foot-soc{position:absolute;left:160px;top:2668px;display:flex;gap:4px}
.foot-soc .soc{width:28px;height:28px;background:var(--greyorange)}
.foot-soc .soc:first-child{background:var(--orange)}
.col{position:absolute;top:2562px}
.col h4{font-size:17px;font-weight:500;margin-bottom:12px}
.col li{list-style:none;font-size:12px;line-height:21px}
.col.contact li{display:flex;align-items:center;gap:8px;font-size:12.5px;line-height:30px}
.col.contact .ic{background:var(--orange);width:21px;height:21px}
.rule{position:absolute;left:0;top:2775px;width:1200px;height:1px;background:#e5e0da}
.legal{position:absolute;top:2793px;font-size:12px}
</style>
</head>
<body>

<div class="hero-photo" role="img" aria-label="Photo of the teacher seated on a mat in a bright studio, smiling in a twist"></div>
<svg class="hero-wave" width="1200" height="545" viewBox="0 0 1200 545">
  <defs><linearGradient id="fade" x1="0" x2="1"><stop offset="0" stop-color="#f8f3ec"/><stop offset=".45" stop-color="#f8f3ec" stop-opacity=".6"/><stop offset=".6" stop-color="#f8f3ec" stop-opacity="0"/></linearGradient></defs>
  <rect width="1200" height="545" fill="url(#fade)"/>
  <path d="M0 412 C170 470 330 535 470 533 C640 530 900 450 1200 348 L1200 545 L0 545 Z" fill="#fff"/>
</svg>

<header class="site-header">
  <div class="brand"><span class="brand-dot"></span>Liesbet Oonwerk</div>
  <nav class="nav">
    <a href="#">Home</a><a href="#">Kavenda Structural Integration</a><a href="#">Movement</a><a href="#">About Me</a><a href="#">Events</a><a href="#" class="active">Work with Me</a>
  </nav>
  <div class="btn-book">Book a Session</div>
</header>

<div class="hero-text">
  <div class="eyebrow">COLLABORATE</div>
  <h1 class="hero-title">Work with <span>Me</span></h1>
  <p class="hero-sub">For studios, organisations and teacher training schools.</p>
</div>

<div class="ghost">Work with Me</div>
<h2 class="section-title">Ways we can work together</h2>
<div class="divider" style="left:541px;top:686px;width:84px"></div>
<p class="intro">Explore meaningful ways to deepen your practice, expand your understanding, and connect with a supportive community. Each offering is designed to guide you toward greater embodiment, awareness, and personal transformation.</p>

<div class="card" style="left:107px;top:876px"><div class="card-icon" role="img" aria-label="Line illustration of hands-on teaching"></div><h3>Guest teaching</h3><p>Invite me to bring embodied movement, Kavenda, and somatic wisdom into your space through workshops, retreats, or special events tailored to your community</p><div class="btn-start">GET STARTED <svg width="8" height="12" viewBox="0 0 8 12"><path d="M2 1l5 5-5 5" stroke="#fff" stroke-width="2" fill="none"/></svg></div></div>
<div class="card" style="left:452px;top:876px"><div class="card-icon" role="img" aria-label="Line illustration of a seated group"></div><h3>Workshops</h3><p>Hands-on experiences that blend movement, body awareness, and practical tools to help you reconnect with your body and create lasting transformation.</p><div class="btn-start">GET STARTED <svg width="8" height="12" viewBox="0 0 8 12"><path d="M2 1l5 5-5 5" stroke="#fff" stroke-width="2" fill="none"/></svg></div></div>
<div class="card" style="left:796px;top:876px"><div class="card-icon" role="img" aria-label="Line illustration of a spine and torso"></div><h3>Anatomy</h3><p>Develop a deeper understanding of the body through accessible anatomy education that supports movement, alignment, and embodied practice.</p><div class="btn-start">GET STARTED <svg width="8" height="12" viewBox="0 0 8 12"><path d="M2 1l5 5-5 5" stroke="#fff" stroke-width="2" fill="none"/></svg></div></div>

<div class="card" style="left:105px;top:1256px"><div class="card-icon" role="img" aria-label="Line illustration of a pose sequence"></div><h3>Sequencing</h3><p>Learn how to create intentional, balanced sequences that support nervous system regulation, mobility, and a more integrated movement experience.</p><div class="btn-start">GET STARTED <svg width="8" height="12" viewBox="0 0 8 12"><path d="M2 1l5 5-5 5" stroke="#fff" stroke-width="2" fill="none"/></svg></div></div>
<div class="card" style="left:449px;top:1256px"><div class="card-icon" role="img" aria-label="Line illustration of a teacher at a board"></div><h3>Teacher development</h3><p>Personalized mentorship and training for teachers looking to refine their skills, strengthen their voice, and deepen their confidence in guiding others.</p><div class="btn-start">GET STARTED <svg width="8" height="12" viewBox="0 0 8 12"><path d="M2 1l5 5-5 5" stroke="#fff" stroke-width="2" fill="none"/></svg></div></div>
<div class="card" style="left:793px;top:1256px"><div class="card-icon" role="img" aria-label="Line illustration of an open book with a lotus"></div><h3>Continuing education</h3><p>Expand your knowledge with advanced trainings and immersive learning experiences designed to support your growth as a practitioner and lifelong student.</p><div class="btn-start">GET STARTED <svg width="8" height="12" viewBox="0 0 8 12"><path d="M2 1l5 5-5 5" stroke="#fff" stroke-width="2" fill="none"/></svg></div></div>

<svg class="abs" style="left:0;top:1635px" width="1200" height="630" viewBox="0 0 1200 630">
  <defs><linearGradient id="photo2" x1="0" x2="1" y1="0" y2="1"><stop offset="0" stop-color="#efe4d6"/><stop offset=".35" stop-color="#a85d43"/><stop offset=".6" stop-color="#c9674a"/><stop offset="1" stop-color="#d9b38a"/></linearGradient></defs>
  <path d="M0 120 L600 0 L1200 0 L1200 630 L0 630 Z" fill="#f6f1eb"/>
  <path d="M580 20 C720 10 860 60 1200 150 L1200 630 L580 630 Z" fill="url(#photo2)" role="img" aria-label="Photo of the teacher sitting on the floor writing in a notebook beside a laptop"/>
</svg>
<div class="collab-text">
  <h2>Let’s collaborate something meaningful together.</h2>
  <p class="collab-lead">Private sessions are available for those seeking individual support.</p>
  <p class="collab-body">These sessions are shaped around your specific needs and goals, whether you want to deepen your practice, recover from injury, or move with greater ease. A quieter, more personal space to explore your body and movement.</p>
</div>
<div class="divider" style="left:133px;top:1883px;width:86px"></div>
<div class="btn-dark">WORK WITH ME <svg width="8" height="12" viewBox="0 0 8 12"><path d="M2 1l5 5-5 5" stroke="#fff" stroke-width="2" fill="none"/></svg></div>

<section class="band">
  <h2>Stay Connected</h2>
  <p class="band-sub">Receive updates about workshops, trainings, retreats and new offerings.</p>
  <div class="input">Email address*</div>
  <div class="btn-sub">SUBSCRIBE NOW <svg width="14" height="10" viewBox="0 0 14 10"><path d="M0 5h12M8 1l4 4-4 4" stroke="#fff" stroke-width="1.6" fill="none"/></svg></div>
  <div class="vline"></div>
  <div class="band-contact" style="top:64px"><span class="ic"><svg width="12" height="9" viewBox="0 0 12 9"><rect x=".5" y=".5" width="11" height="8" fill="none" stroke="#2f4f4f"/><path d="M.5 .5l5.5 4 5.5-4" stroke="#2f4f4f" fill="none"/></svg></span><u>info@liesbetoonwerk.com</u></div>
  <div class="band-contact" style="top:95px"><span class="ic"><svg width="11" height="11" viewBox="0 0 11 11"><path d="M2 1l2 2-1 1.5a6 6 0 0 0 3.5 3.5L8 7l2 2-1.5 1.5C4 10 1 7 .5 2.5Z" fill="#2f4f4f"/></svg></span>(+123) 555 0142</div>
  <div class="band-contact socials" style="top:131px"><span class="soc"></span><span class="soc"></span><span class="soc"></span></div>
</section>

<div class="foot-brand"><div class="brand-dot"></div>Liesbet Oonwerk</div>
<div class="foot-soc"><span class="soc"></span><span class="soc"></span><span class="soc"></span></div>

<div class="col contact" style="left:358px"><h4>Contact Us</h4><ul>
  <li><span class="ic"></span>info@liesbetoonwerk.com</li>
  <li><span class="ic"></span>(+123) 555 0142</li>
  <li><span class="ic"></span>Location City</li></ul></div>
<div class="col" style="left:561px;top:2564px"><h4>Quick Links</h4><ul>
  <li>Home</li><li>Kavenda Structural Integration</li><li>Movement</li><li>About Me</li><li>Events</li></ul></div>
<div class="col" style="left:769px;top:2564px"><h4>Services</h4><ul>
  <li>Yoga classes</li><li>Pilates classes</li><li>Teacher trainings</li><li>Workshops</li><li>Retreats</li></ul></div>
<div class="col" style="left:932px"><h4>Resources</h4><ul>
  <li>Work with Me</li><li>Testimonials</li><li>Book a Session</li><li>Contact</li></ul></div>

<div class="rule"></div>
<div class="legal" style="left:137px">Copyright © 2026 Liesbet Oonwerk. All Right Reserved</div>
<div class="legal" style="left:851px">Privacy Policy &nbsp;&nbsp;&nbsp; Terms &amp; Conditions</div>

</body>
</html>
```